Wine Label front and back

Need a front and back label. Front design is attached but want it fixed up and made eye catching Back label is going to be basic info attached as well. On the front label we will need Alc.By Vol. 14.8% and 2017 Sauvignon Blanc, Green Valley somewhere on the label.

Colors
fbf289
fbee3e
fdf9cf
cadf82
ec1f27

```html
<!DOCTYPE html>
<html lang="en">
<head>
<meta charset="utf-8">
<title>Marivale Vineyards – Sauvignon Blanc 2017 Front Label</title>
<link href="https://fonts.googleapis.com/css2?family=Cinzel:wght@400;600&display=swap" rel="stylesheet">
<style>
  :root {
    --page-bg: #ffffff;
    --label-paper: #f6f6f6;
    --label-edge: #e4e4e4;
    --brand-red: #b5353e;
    --ink: #3a3a3a;
    --leaf-light: #cadf82;
    --leaf-mid: #8fd43a;
    --leaf-deep: #5fb82a;
    --vine-stem: #a39a5a;
  }
  * { box-sizing: border-box; margin: 0; padding: 0; }
  html, body {
    width: 1200px;
    height: 1200px;
    overflow: hidden;
    background: var(--page-bg);
  }
  .canvas {
    position: relative;
    width: 1200px;
    height: 1200px;
  }
  .front-label {
    position: absolute;
    left: 150px;
    top: 130px;
    width: 900px;
    height: 940px;
    background: linear-gradient(90deg, var(--label-paper) 0%, #fbfbfb 45%, var(--label-edge) 100%);
    font-family: "Cinzel", "Times New Roman", serif;
    color: var(--ink);
  }
  .brand {
    position: absolute;
    left: 0;
    right: 0;
    top: 70px;
    text-align: center;
    color: var(--brand-red);
    font-weight: 400;
    line-height: 1;
  }
  .brand-name {
    display: block;
    font-size: 92px;
    letter-spacing: 2px;
  }
  .brand-sub {
    display: block;
    margin-top: 12px;
    font-size: 32px;
    letter-spacing: 9px;
  }
  .vine-art {
    position: absolute;
    left: 95px;
    top: 260px;
    width: 700px;
    height: 450px;
  }
  .varietal {
    position: absolute;
    left: 0;
    right: 0;
    top: 725px;
    text-align: center;
    font-size: 62px;
    font-weight: 400;
    letter-spacing: 1px;
    color: var(--ink);
  }
  .details {
    position: absolute;
    left: 50px;
    right: 50px;
    top: 845px;
    height: 72px;
    display: flex;
    align-items: center;
    justify-content: space-between;
  }
  .details-item {
    flex: 1;
    text-align: center;
    font-size: 24px;
    letter-spacing: 1px;
  }
  .details-item.vintage {
    flex: 0 0 220px;
    font-size: 46px;
  }
  .details-rule {
    width: 3px;
    height: 72px;
    background: var(--ink);
  }
</style>
</head>
<body>
<main class="canvas">
  <section class="front-label">
    <h1 class="brand">
      <span class="brand-name">Marivale</span>
      <span class="brand-sub">Vineyards</span>
    </h1>

    <svg class="vine-art" viewBox="0 0 700 450" role="img" aria-label="Illustration of a bright green grape vine leaf on a curling tendril">
      <defs>
        <radialGradient id="leafTone" cx="50%" cy="45%" r="60%">
          <stop offset="0%" stop-color="var(--leaf-light)"/>
          <stop offset="55%" stop-color="var(--leaf-mid)"/>
          <stop offset="100%" stop-color="var(--leaf-deep)"/>
        </radialGradient>
      </defs>
      <ellipse cx="400" cy="230" rx="270" ry="200" fill="url(#leafTone)" opacity="0.55"/>
    </svg>

    <h2 class="varietal">Sauvignon Blanc</h2>

    <div class="details">
      <p class="details-item abv">Alc.By Vol. 14.8%</p>
      <span class="details-rule"></span>
      <p class="details-item vintage">2017</p>
      <span class="details-rule"></span>
      <p class="details-item region">Green Valley</p>
    </div>
  </section>
</main>
</body>
</html>
```